New web design needed for our company

We need our website designing, it needs to be professional and look creative,
We are a plumbing and heating company called Kestrel Bay's (www.kestrelbays.co.uk)
I like this site design also some of the following maybe:
https://www.marnockheating.com/
http://www.tavelpower.co.uk

Please let me know when you want our logo files as it wont let me upload them

The design will require coding once the design is complete, i havent paid for this yet as i want to be sure the design is good before i commit.

The template needs to look professional and look like one of the leading companies.
The site will consist of all the features this site has https://www.marnockheating.com/

I like a modern design with the latest technology.

Must have a customer login page and a my account area

Target Market(s)

Everyone

Industry/Entity Type

Plumbing

Coding

Coded - Design and coding required

Number of Pages Required

5+ page

Font styles to use
Other font styles liked:
• whatever suites

Requirements
Must have
• The design will require coding once the design is complete, i havent paid for this yet as i want to be sure the design is good before i commit.
• The template needs to look professional and look like one of the leading companies.
• The site will consist of all the features this site has https://www.marnockheating.com/
• I like a modern design with the latest technology.
• Must have a customer login page and a my account area
Nice to have
• inspirational and different
Should not have
• plain boring designs like most plumbing websites, needs to be inspiring and attract people from first sight.

```html
<!DOCTYPE html>
<html lang="en">
<head>
<meta charset="utf-8">
<title>Kestrel Bay's – Plumbing &amp; Heating</title>
<link href="https://fonts.googleapis.com/css2?family=Ubuntu:wght@400;500;700&display=swap" rel="stylesheet">
<style>
:root{
  --navy:#0b2d6b;
  --navy-text:#1d4a86;
  --orange:#ff5a3c;
  --green:#6ab04c;
  --white:#ffffff;
  --body-text:#2b5a93;
}
*{box-sizing:border-box;margin:0;padding:0}
html,body{width:1200px;height:1192px;overflow:hidden;background:var(--white);font-family:'Ubuntu',sans-serif}
.page{position:relative;width:1200px;height:1192px}
.abs{position:absolute}

.utility-bar{left:0;top:21px;width:1200px;height:41px;background:var(--navy)}
.utility-link{top:21px;height:41px;line-height:41px;color:var(--white);font-size:14px}
.search{left:951px;top:21px;width:202px;height:41px;background:var(--orange);display:flex;align-items:center;justify-content:space-between;padding:0 12px 0 20px;color:#ffd9cf;font-size:11px}

.brand{left:45px;top:86px;display:flex;align-items:center;gap:8px}
.brand-mark{width:14px;height:14px;border-radius:50%;background:var(--orange)}
.brand-name{font-size:34px;font-weight:700;color:var(--navy);letter-spacing:-0.5px;line-height:40px}

.main-nav{top:102px;left:435px;display:flex;gap:34px;font-size:15px;font-weight:500;color:var(--navy-text)}
.main-nav span{display:flex;align-items:center;gap:6px}
.caret{width:0;height:0;border-left:4px solid transparent;border-right:4px solid transparent;border-top:5px solid var(--navy-text)}

.hero{left:41px;top:160px;width:1113px;height:321px;
  background:
    radial-gradient(ellipse 160px 200px at 82% 62%, rgba(40,80,160,.85), rgba(40,80,160,0) 100%),
    radial-gradient(ellipse 120px 90px at 86% 62%, rgba(70,170,230,.8), rgba(70,170,230,0) 100%),
    radial-gradient(ellipse 300px 70px at 30% 18%, rgba(255,255,255,.9), rgba(255,255,255,0) 100%),
    radial-gradient(ellipse 260px 60px at 70% 14%, rgba(255,255,255,.85), rgba(255,255,255,0) 100%),
    radial-gradient(ellipse 420px 160px at 88% 45%, rgba(200,170,120,.75), rgba(200,170,120,0) 100%),
    linear-gradient(180deg,#a9bfd8 0%,#d9e3ee 30%,#c9b596 58%,#8a7a5e 82%,#4f4a3c 100%)}
.hero-title{left:41px;top:304px;width:425px;height:64px;background:var(--navy);color:var(--white);font-size:26px;line-height:64px;padding-left:37px}
.hero-cta{left:310px;top:388px;width:154px;height:34px;background:var(--orange);color:var(--white);font-size:18px;line-height:34px;text-align:center}

.chat-tab{left:1160px;top:384px;width:40px;height:166px;background:var(--green);border-radius:6px 0 0 6px;color:var(--white);font-size:15px;font-weight:500;writing-mode:vertical-rl;transform:rotate(180deg);display:flex;align-items:center;justify-content:center}

.section-title{left:47px;top:502px;font-size:20px;font-weight:500;color:var(--navy-text)}

.feature{top:564px;width:255px;text-align:center}
.feature-media{width:255px;height:128px;border-radius:6px}
.feature-title{margin-top:12px;font-size:17px;font-weight:500;color:var(--navy-text);line-height:22px}
.feature-text{margin:2px auto 0;width:218px;font-size:12px;line-height:22px;color:var(--body-text)}

.service{top:829px;width:349px;height:296px}
.service-media{width:349px;height:198px;border-radius:6px 6px 0 0}
.service-label{position:absolute;left:0;top:142px;height:56px;background:var(--navy);color:var(--white);font-size:16px;font-weight:700;line-height:56px;padding:0 30px}
.service-action{width:349px;height:98px;background:var(--orange);border-radius:0 0 6px 6px;color:var(--white);font-size:14px;font-weight:700;line-height:21px;padding:26px 40px 0 43px;position:relative}
.service-action::before{content:"+";position:absolute;left:24px;top:26px;font-size:13px}
</style>
</head>
<body>
<div class="page">

  <header>
    <div class="abs utility-bar"></div>
    <a class="abs utility-link" style="left:818px">Login</a>
    <a class="abs utility-link" style="left:878px">Sign Up</a>
    <div class="abs search">
      <span>Search</span>
      <svg width="18" height="18" viewBox="0 0 18 18" aria-hidden="true"><circle cx="7.5" cy="7.5" r="5.5" fill="none" stroke="#fff" stroke-width="2.4"/><line x1="11.5" y1="11.5" x2="16.5" y2="16.5" stroke="#fff" stroke-width="2.8" stroke-linecap="round"/></svg>
    </div>

    <div class="abs brand">
      <span class="brand-name">Kestrel Bay's</span>
      <span class="brand-mark"></span>
    </div>

    <nav class="abs main-nav">
      <span>Do it online <i class="caret"></i></span>
      <span>Our services <i class="caret"></i></span>
      <span>Commercial <i class="caret"></i></span>
      <span>Help &amp; advice <i class="caret"></i></span>
      <span>About us <i class="caret"></i></span>
      <span>Contact us</span>
    </nav>
  </header>

  <section>
    <div class="abs hero" role="img" aria-label="Engineer holding coiled blue pipe in front of suburban houses under a cloudy sky"></div>
    <div class="abs hero-title">Great Value Boiler Installations</div>
    <div class="abs hero-cta">More info &gt;</div>
  </section>

  <div class="abs chat-tab">Chat with us live</div>

  <h2 class="abs section-title">How can we help you today?</h2>

  <div class="abs feature" style="left:46px">
    <div class="feature-media" role="img" aria-label="Boiler cashback scheme promotional graphic" style="background:radial-gradient(ellipse 120px 24px at 50% 80%, rgba(240,170,30,.55), rgba(240,170,30,0) 100%),radial-gradient(ellipse 130px 40px at 50% 45%, rgba(255,255,255,.18), rgba(255,255,255,0) 100%),linear-gradient(180deg,#45474b,#2f3134)"></div>
    <h3 class="feature-title">London Boilers</h3>
    <p class="feature-text">Find out if you're eligible to get £400 Cashback as part of the new London replacement boiler scheme.</p>
  </div>
  <div class="abs feature" style="left:330px">
    <div class="feature-media" role="img" aria-label="Pink piggy bank with a coin being dropped in" style="background:radial-gradient(ellipse 45px 40px at 46% 55%, rgba(245,140,190,.95), rgba(245,140,190,0) 100%),linear-gradient(180deg,#c3cfdc,#dde4ec 80%,#eef1f4)"></div>
    <h3 class="feature-title">Financing Available</h3>
    <p class="feature-text">Make paying for your new boiler more manageable by spreading the cost or deferring payment.</p>
  </div>
  <div class="abs feature" style="left:613px">
    <div class="feature-media" role="img" aria-label="Map of the South East and London service area" style="background:radial-gradient(ellipse 70px 40px at 90% 20%, rgba(150,195,240,.95), rgba(150,195,240,0) 100%),radial-gradient(ellipse 120px 30px at 60% 105%, rgba(150,195,240,.95), rgba(150,195,240,0) 100%),radial-gradient(ellipse 90px 40px at 40% 60%, rgba(200,225,160,.9), rgba(200,225,160,0) 100%),linear-gradient(135deg,#ece9d2,#dfe7c4)"></div>
    <h3 class="feature-title">Areas We Cover</h3>
    <p class="feature-text">We cover the entirety of the South East and London. Check if we cover your area.</p>
  </div>
  <div class="abs feature" style="left:896px">
    <div class="feature-media" role="img" aria-label="Branded white company vans parked together" style="background:radial-gradient(ellipse 90px 50px at 65% 45%, rgba(255,255,255,.95), rgba(255,255,255,0) 100%),radial-gradient(ellipse 60px 25px at 55% 95%, rgba(40,40,45,.6), rgba(40,40,45,0) 100%),linear-gradient(180deg,#dfe4ea,#b9c0c9)"></div>
    <h3 class="feature-title">Do we look familiar?</h3>
    <p class="feature-text">We've been running TV adverts on Brightview TV &amp; Northstar for years - check out some of our recent work.</p>
  </div>

  <div class="abs service" style="left:45px">
    <div class="service-media" role="img" aria-label="Close-up of a boiler control panel" style="background:radial-gradient(ellipse 60px 40px at 22% 30%, rgba(120,150,200,.55), rgba(120,150,200,0) 100%),radial-gradient(ellipse 50px 30px at 55% 25%, rgba(120,150,200,.45), rgba(120,150,200,0) 100%),linear-gradient(160deg,#f1f3f5,#c6ccd3 70%,#a9b0b9)"></div>
    <div class="service-label">Buy a New Boiler</div>
    <div class="service-action">Get your free online boiler estimate using our easy online tool.</div>
  </div>
  <div class="abs service" style="left:424px">
    <div class="service-media" role="img" aria-label="Heating maintenance contract renewal form" style="background:radial-gradient(ellipse 150px 60px at 55% 40%, rgba(235,238,246,.9), rgba(235,238,246,0) 100%),linear-gradient(150deg,#6f6a66,#b9bfcc 45%,#9aa3b8 100%)"></div>
    <div class="service-label">Cover &amp; Maintenance</div>
    <div class="service-action">Get protected from as little as £13 per month.</div>
  </div>
  <div class="abs service" style="left:802px">
    <div class="service-media" role="img" aria-label="Engineer repairing the inside of a boiler" style="background:radial-gradient(ellipse 80px 90px at 22% 45%, rgba(190,205,225,.9), rgba(190,205,225,0) 100%),radial-gradient(ellipse 70px 70px at 75% 45%, rgba(90,85,75,.7), rgba(90,85,75,0) 100%),linear-gradient(135deg,#d2d5da,#9a978f 55%,#dcd8d0)"></div>
    <div class="service-label">Breakdown &amp; Repair</div>
    <div class="service-action">Book a visit from one of our expertly trained team.</div>
  </div>

</div>
</body>
</html>
```